Tolvane - online store for farm produce

Online store selling fresh produce (vegetables, fruits, dairy products, meat, ...) from various farmers. Every farm has its own shopping window - order page - just like a really simple web store.

Please check the attached design brief and mock-ups for further details.

Target Market(s)

People looking for fresh vegetables, fruit, meat, ... delivered from farms

Industry/Entity Type

Farming

Coding

Coded - Design and coding required

Number of Pages Required

5+ page

Font styles to use
Sans Serif

Requirements
Must have
• Custom design. Good UX/UI design, very functional.
Responsive using bootstrap 12 point grid system

```html
<!DOCTYPE html>
<html lang="en">
<head>
<meta charset="utf-8">
<title>Tolvane – Farm Produce Store</title>
<link href="https://fonts.googleapis.com/css2?family=Poppins:wght@400;500;600;700&display=swap" rel="stylesheet">
<style>
:root{
  --page-bg:#f3f4f6;
  --green:#47c49b;
  --green-soft:#a8dcc7;
  --forest:#3e5a3e;
  --heading:#2f4a33;
  --text:#6b6f6c;
  --line:#d9ddd8;
  --white:#ffffff;
  --map:#eceeec;
}
*{box-sizing:border-box;margin:0;padding:0}
html,body{width:722px;height:1200px;overflow:hidden;background:var(--page-bg)}
body{font-family:"Poppins",sans-serif;color:var(--text)}
.stage{position:absolute;left:0;top:0;width:1484px;height:2468px;transform:scale(.4862);transform-origin:0 0}
.mockup{position:absolute;top:284px;height:1900px;background:var(--white);overflow:hidden}
.mockup--mobile{left:193px;width:246px}
.mockup--desktop{left:517px;width:774px}
.abs{position:absolute}
.shape{position:absolute;left:0;top:0}
.brand{position:absolute;display:flex;align-items:center;gap:5px;font-family:"Poppins",sans-serif;font-weight:700;color:var(--white);letter-spacing:.5px}
.brand__dot{width:7px;height:7px;border-radius:50%;background:var(--green)}
.hero-title{position:absolute;left:0;right:0;text-align:center;color:var(--white);font-weight:700}
.hero-text{position:absolute;text-align:center;color:var(--white);line-height:1.55}
.btn{position:absolute;display:flex;align-items:center;justify-content:center;border-radius:20px;font-weight:500;color:var(--green);letter-spacing:.3px;text-transform:uppercase;white-space:nowrap}
.btn--solid{background:var(--white)}
.btn--outline{border:1.5px solid var(--green);background:var(--white)}
.section-title{position:absolute;font-weight:700;color:var(--heading);text-transform:uppercase;letter-spacing:.2px}
.ticks{position:absolute;list-style:none}
.ticks li{position:relative;padding-left:16px;white-space:nowrap}
.ticks li::before{content:"";position:absolute;left:0;top:50%;width:8px;height:8px;margin-top:-5px;border:1px solid var(--green);border-radius:50%}
.ticks li::after{content:"";position:absolute;left:3px;top:50%;width:2px;height:4px;margin-top:-4px;border:solid var(--green);border-width:0 1px 1px 0;transform:rotate(45deg)}
.ticks--light li{color:var(--white)}
.ticks--light li::before{border-color:var(--white)}
.ticks--light li::after{border-color:var(--white)}
.photo{position:absolute}
.nav{position:absolute;display:flex;align-items:center;font-size:8px;font-weight:500;color:var(--white);text-transform:uppercase}
.nav__item{margin-right:24px}
.nav__item--active{color:var(--green)}
.icon-circle{position:absolute;border-radius:50%;background:var(--white);display:flex;align-items:center;justify-content:center}
.icon-circle--green{background:var(--green)}
.cart{position:absolute;background:var(--green);color:var(--white);border-radius:14px;font-size:8px;font-weight:600;display:flex;align-items:center;justify-content:center;gap:6px}
.card{position:absolute;background:var(--white);box-shadow:0 2px 8px rgba(0,0,0,.07);text-align:center}
.card--active{border:1px solid var(--green)}
.card__img{position:absolute;left:50%;border-radius:50%}
.card__rule{position:absolute;left:50%;height:2px;background:var(--green)}
.card__name{position:absolute;left:0;right:0;color:#3d3f3d;text-transform:uppercase;line-height:1.5}
.card__price{position:absolute;left:0;right:0;color:var(--green);font-weight:500}
.card__price small{color:var(--text);font-size:.55em;font-weight:400}
.card__tools{position:absolute;left:0;right:0;display:flex;justify-content:center;gap:6px}
.card__tools span{width:18px;height:18px;border-radius:50%;background:var(--forest)}
.card__tools span:first-child{background:var(--green)}
.arrow{position:absolute;border:1px solid var(--green);border-radius:50%;display:flex;align-items:center;justify-content:center;background:var(--white)}
.arrow::before{content:"";width:4px;height:4px;border:solid var(--green);border-width:0 1px 1px 0}
.arrow--prev::before{transform:rotate(135deg);margin-left:2px}
.arrow--next::before{transform:rotate(-45deg);margin-right:2px}
.footer{position:absolute;left:0;right:0;background:var(--forest)}
.farm{position:absolute;text-align:center;color:var(--white)}
.farm__title{color:var(--green);font-weight:500}
.map{position:absolute;background:var(--map)}
.socials{position:absolute;display:flex;gap:6px}
.socials span{border-radius:50%;border:1px solid var(--white)}
.socials span.is-active{background:var(--green);border-color:var(--green)}
.copyright{position:absolute;left:0;right:0;text-align:center;color:var(--white)}
.copyright em{font-style:normal;color:var(--green)}
</style>
</head>
<body>
<div class="stage">

  <!-- MOBILE LAYOUT -->
  <section class="mockup mockup--mobile">
    <svg class="shape" width="246" height="240" viewBox="0 0 246 240">
      <defs>
        <linearGradient id="heroMob" x1="0" y1="0" x2="0" y2="1">
          <stop offset="0" stop-color="#8a6a4a"/><stop offset=".55" stop-color="#a6733a"/><stop offset="1" stop-color="#2e241a"/>
        </linearGradient>
      </defs>
      <path d="M0 188 Q120 240 246 196 V214 Q120 262 0 204Z" fill="#d9ddd8"/>
      <path d="M0 180 Q120 232 246 188 V204 Q120 250 0 194Z" fill="#a8dcc7"/>
      <path d="M0 0H246V196 Q120 236 0 180Z" fill="url(#heroMob)" role="img" aria-label="Photo of two farmers shaking hands in a field at sunset"/>
    </svg>
    <div class="brand" style="left:12px;top:17px;font-size:15px"><span>Tolvane</span><span class="brand__dot"></span></div>
    <div class="icon-circle" style="left:164px;top:16px;width:18px;height:18px"></div>
    <div class="icon-circle icon-circle--green" style="left:191px;top:16px;width:18px;height:18px"></div>
    <svg class="abs" style="left:219px;top:21px" width="10" height="8"><path d="M0 1H10M0 4H10M0 7H10" stroke="#fff" stroke-width="1"/></svg>
    <h1 class="hero-title" style="top:78px;font-size:12.5px">WHAT IS THIS ABOUT US</h1>
    <p class="hero-text" style="left:12px;width:222px;top:100px;font-size:7.6px">Lorem Ipsum is simply dummy text of the printing and typesetting industry. Lorem Ipsum has been the industry's standard...</p>
    <div class="btn btn--solid" style="left:71px;top:154px;width:104px;height:18px;font-size:6.8px">Product search</div>

    <div class="photo" role="img" aria-label="Photo of a smiling woman handing vegetables at a market stall" style="left:25px;top:254px;width:193px;height:200px;border-radius:46% 54% 42% 58% / 52% 40% 60% 48%;background:radial-gradient(circle at 40% 35%,#e4d2c0,#b98b6a 45%,#6f8a4e 80%)"></div>
    <h2 class="section-title" style="left:12px;top:472px;font-size:10px">Customer benefits</h2>
    <ul class="ticks" style="left:12px;top:499px;font-size:7.6px;line-height:17.6px">
      <li>Lorem Ipsum is simply dummy text work ipsum</li>
      <li>Readable content of a page looking at its lorem</li>
      <li>Lorem Ipsum is simply dummy text work ipsum</li>
      <li>Readable content of a page looking at its lorem</li>
      <li>Lorem Ipsum is simply dummy text work ipsum</li>
    </ul>
    <div class="btn btn--outline" style="left:12px;top:597px;width:94px;height:18px;font-size:6.8px">Product search</div>

    <svg class="shape" style="top:625px" width="246" height="170" viewBox="0 0 246 170">
      <defs>
        <linearGradient id="farmMob" x1="0" y1="0" x2="1" y2="0">
          <stop offset=".1" stop-color="#47c49b"/><stop offset=".5" stop-color="#8fb07c"/><stop offset="1" stop-color="#a98a62"/>
        </linearGradient>
      </defs>
      <path d="M0 0 Q120 40 246 8 V14 Q120 30 0 16Z" fill="#d9ddd8"/>
      <path d="M0 16 Q120 30 246 14 V162 Q150 120 0 132Z" fill="url(#farmMob)" role="img" aria-label="Photo of a farmer carrying a basket of fresh vegetables"/>
      <path d="M0 132 Q150 120 246 162 V170 Q150 128 0 140Z" fill="#d9ddd8"/>
    </svg>
    <h2 class="section-title" style="left:12px;top:804px;font-size:10px">Farmer benefits</h2>
    <ul class="ticks" style="left:12px;top:831px;font-size:7.6px;line-height:17.6px">
      <li>Lorem Ipsum is simply dummy text work ipsum</li>
      <li>Readable content of a page looking at its lorem</li>
      <li>Lorem Ipsum is simply dummy text work ipsum</li>
      <li>Readable content of a page looking at its lorem</li>
      <li>Lorem Ipsum is simply dummy text work ipsum</li>
    </ul>
    <div class="btn btn--outline" style="left:12px;top:929px;width:94px;height:18px;font-size:6.8px">Tell me more</div>

    <h2 class="section-title" style="left:12px;top:980px;font-size:10px">Featured products</h2>
    <div class="arrow arrow--prev" style="left:189px;top:978px;width:18px;height:18px"></div>
    <div class="arrow arrow--next" style="left:215px;top:978px;width:18px;height:18px"></div>
    <div class="card" style="left:12px;top:1010px;width:105px;height:170px">
      <div class="card__img" role="img" aria-label="Photo of kiwi fruit" style="top:24px;width:74px;height:54px;margin-left:-37px;background:radial-gradient(circle at 35% 55%,#7bbf3a 30%,#8a6a3a 70%)"></div>
      <div class="card__rule" style="top:97px;width:34px;margin-left:-17px"></div>
      <p class="card__name" style="top:106px;font-size:7px">Curabitur volut-<br>pat nulla non sem</p>
      <p class="card__price" style="top:138px;font-size:11px">€2 <small>/ 1 KG</small></p>
    </div>
    <div class="card" style="left:130px;top:1010px;width:105px;height:170px">
      <div class="card__img" role="img" aria-label="Photo of fresh tomatoes" style="top:20px;width:68px;height:62px;margin-left:-34px;background:radial-gradient(circle at 45% 45%,#f25a3c,#c8201a)"></div>
      <div class="card__rule" style="top:97px;width:34px;margin-left:-17px"></div>
      <p class="card__name" style="top:106px;font-size:7px">Curabitur volut-<br>pat nulla non sem</p>
      <p class="card__price" style="top:138px;font-size:11px">€4 <small>/ 2 KG</small></p>
    </div>

    <div class="footer" style="top:1215px;height:685px">
      <div class="brand" style="left:0;right:0;justify-content:center;top:22px;font-size:24px"><span>Tolvane</span><span class="brand__dot" style="width:10px;height:10px"></span></div>
      <div class="farm" style="left:12px;width:222px;top:64px;font-size:7.4px;line-height:1.45">
        <p class="farm__title" style="font-size:9.5px">01 - Lorem Ipsum Farm</p>
        <p>418 Orchard Hollow Rd,<br>Brenly ML 40215</p>
      </div>
      <div class="map" role="img" aria-label="Street map of the farm location" style="left:12px;top:120px;width:222px;height:105px"></div>
      <div class="farm" style="left:12px;width:222px;top:247px;font-size:7.4px;line-height:1.45">
        <p class="farm__title" style="font-size:9.5px">01 - Lorem Ipsum Farm</p>
        <p>418 Orchard Hollow Rd,<br>Brenly ML 40215</p>
      </div>
      <div class="map" role="img" aria-label="Street map of the farm location" style="left:12px;top:303px;width:222px;height:105px"></div>
      <div class="farm" style="left:12px;width:222px;top:429px;font-size:7.4px;line-height:1.45">
        <p class="farm__title" style="font-size:9.5px">01 - Lorem Ipsum Farm</p>
        <p>418 Orchard Hollow Rd,<br>Brenly ML 40215</p>
      </div>
      <div class="map" role="img" aria-label="Street map of the farm location" style="left:12px;top:485px;width:222px;height:105px"></div>
      <div class="socials" style="left:89px;top:614px"><span style="width:18px;height:18px"></span><span class="is-active" style="width:18px;height:18px"></span><span style="width:18px;height:18px"></span></div>
      <p class="copyright" style="top:648px;font-size:7.6px">© 2020 <em>Tolvane.</em> All Rights Reserved</p>
    </div>
  </section>

  <!-- DESKTOP LAYOUT -->
  <section class="mockup mockup--desktop">
    <svg class="shape" width="774" height="460" viewBox="0 0 774 460">
      <defs>
        <linearGradient id="heroDesk" x1="0" y1="0" x2="0" y2="1">
          <stop offset="0" stop-color="#8a6d52"/><stop offset=".5" stop-color="#b07a3e"/><stop offset="1" stop-color="#2b2119"/>
        </linearGradient>
      </defs>
      <path d="M0 316 Q180 400 360 440 Q600 470 774 350 V366 Q600 490 360 450 Q180 420 0 330Z" fill="#d9ddd8"/>
      <path d="M0 306 Q180 388 360 426 Q600 454 774 334 V354 Q600 474 360 438 Q180 402 0 320Z" fill="#a8dcc7"/>
      <path d="M0 0H774V334 Q600 448 360 418 Q180 390 0 300Z" fill="url(#heroDesk)" role="img" aria-label="Photo of two farmers shaking hands in a field at sunset"/>
    </svg>
    <div class="brand" style="left:57px;top:16px;font-size:20px"><span>Tolvane</span><span class="brand__dot" style="width:9px;height:9px"></span></div>
    <nav class="nav" style="left:403px;top:21px">
      <span class="nav__item nav__item--active">Home</span>
      <span class="nav__item">Current offers</span>
      <span class="nav__item">Settings</span>
    </nav>
    <div class="icon-circle" style="left:603px;top:17px;width:19px;height:19px"></div>
    <div class="cart" style="left:635px;top:17px;width:82px;height:20px">CART $0.00</div>
    <h1 class="hero-title" style="top:154px;font-size:17px">WHAT IS THIS ABOUT US</h1>
    <p class="hero-text" style="left:147px;width:480px;top:187px;font-size:8.6px">Lorem Ipsum is simply dummy text of the printing and typesetting industry. Lorem Ipsum has been the industry's standard It is a long established fact that a reader will be distracted by the readable content of a page when looking at its layout.</p>
    <div class="btn btn--solid" style="left:341px;top:243px;width:92px;height:19px;font-size:7px">Product search</div>

    <div class="photo" role="img" aria-label="Photo of a smiling woman handing vegetables at a market stall" style="left:68px;top:436px;width:305px;height:312px;border-radius:44% 56% 40% 60% / 50% 40% 60% 50%;background:radial-gradient(circle at 40% 35%,#e6d4c2,#b88a68 42%,#6d8a4e 78%)"></div>
    <h2 class="section-title" style="left:428px;top:524px;font-size:14px">Customer benefits</h2>
    <ul class="ticks" style="left:428px;top:552px;font-size:9.6px;line-height:18.5px">
      <li>Lorem Ipsum is simply dummy text of the printing</li>
      <li>Readable content of a page when looking at its layout</li>
      <li>Lorem Ipsum is simply dummy text of the printing</li>
      <li>Readable content of a page when looking at its layout</li>
      <li>Lorem Ipsum is simply dummy text of the printing</li>
    </ul>
    <div class="btn btn--outline" style="left:428px;top:660px;width:94px;height:20px;font-size:7px">Product search</div>

    <svg class="shape" style="top:760px" width="774" height="440" viewBox="0 0 774 440">
      <defs>
        <linearGradient id="farmDesk" x1="0" y1="0" x2="1" y2="0">
          <stop offset=".45" stop-color="#47c49b"/><stop offset=".7" stop-color="#8caf7a"/><stop offset="1" stop-color="#b08d66"/>
        </linearGradient>
      </defs>
      <path d="M0 8 Q360 80 774 26 V40 Q360 78 0 32Z" fill="#d9ddd8"/>
      <path d="M0 32 Q360 78 774 36 V400 Q400 300 0 360Z" fill="url(#farmDesk)" role="img" aria-label="Photo of a farmer carrying a basket of fresh vegetables"/>
      <path d="M0 360 Q400 300 774 400 V416 Q400 316 0 366Z" fill="#d9ddd8"/>
    </svg>
    <h2 class="section-title" style="left:57px;top:872px;font-size:14px;color:var(--white)">Farmer benefits</h2>
    <ul class="ticks ticks--light" style="left:57px;top:900px;font-size:9.6px;line-height:18.5px">
      <li>Lorem Ipsum is simply</li>
      <li>Readable content lorem</li>
      <li>Lorem Ipsum is simply</li>
      <li>Readable content lorem</li>
      <li>Lorem Ipsum is simply dummy text of the printing</li>
    </ul>
    <ul class="ticks ticks--light" style="left:205px;top:900px;font-size:9.6px;line-height:18.5px">
      <li>Dummy text of the printing</li>
      <li>Page when looking at its layout</li>
      <li>Dummy text of the printing</li>
      <li>Page when looking at its layout</li>
    </ul>
    <div class="btn btn--solid" style="left:57px;top:1008px;width:93px;height:20px;font-size:7px">Tell me more</div>

    <h2 class="section-title" style="left:0;right:0;text-align:center;top:1205px;font-size:14px">Featured products</h2>
    <div class="arrow arrow--prev" style="left:47px;top:1333px;width:18px;height:18px"></div>
    <div class="card" style="left:57px;top:1241px;width:149px;height:191px">
      <div class="card__img" role="img" aria-label="Photo of kiwi fruit" style="top:24px;width:92px;height:62px;margin-left:-46px;background:radial-gradient(circle at 35% 55%,#7bbf3a 30%,#8a6a3a 70%)"></div>
      <div class="card__rule" style="top:102px;width:32px;margin-left:-16px"></div>
      <p class="card__name" style="top:121px;font-size:7.6px">Curabitur volutpat nulla<br>non sem congue</p>
      <p class="card__price" style="top:155px;font-size:12px">€2 <small>/ 1 KG</small></p>
    </div>
    <div class="card" style="left:227px;top:1241px;width:149px;height:191px">
      <div class="card__img" role="img" aria-label="Photo of fresh tomatoes" style="top:16px;width:84px;height:76px;margin-left:-42px;background:radial-gradient(circle at 45% 45%,#f25a3c,#c8201a)"></div>
      <div class="card__rule" style="top:102px;width:32px;margin-left:-16px"></div>
      <p class="card__name" style="top:121px;font-size:7.6px">Curabitur volutpat nulla<br>non sem congue</p>
      <p class="card__price" style="top:155px;font-size:12px">€4 <small>/ 2 KG</small></p>
    </div>
    <div class="card card--active" style="left:397px;top:1241px;width:149px;height:191px">
      <div class="card__img" role="img" aria-label="Photo of beetroot with leaves" style="top:12px;width:72px;height:80px;margin-left:-36px;border-radius:40%;background:linear-gradient(#9fcf7a,#c86a86 60%,#a33d60)"></div>
      <div class="card__tools" style="top:44px"><span></span><span></span><span></span></div>
      <p class="card__name" style="top:121px;font-size:7.6px">Curabitur volutpat nulla<br>non sem congue</p>
      <p class="card__price" style="top:155px;font-size:12px">€2 <small>/ 1 KG</small></p>
    </div>
    <div class="card" style="left:567px;top:1241px;width:149px;height:191px">
      <div class="card__img" role="img" aria-label="Photo of a red onion" style="top:20px;width:80px;height:66px;margin-left:-40px;background:radial-gradient(circle at 40% 50%,#c27aa6,#6e2248)"></div>
      <div class="card__rule" style="top:102px;width:32px;margin-left:-16px"></div>
      <p class="card__name" style="top:121px;font-size:7.6px">Curabitur volutpat nulla<br>non sem congue</p>
      <p class="card__price" style="top:155px;font-size:12px">€2 <small>/ 1 KG</small></p>
    </div>
    <div class="arrow arrow--next" style="left:708px;top:1333px;width:18px;height:18px"></div>
    <div class="btn btn--outline" style="left:330px;top:1453px;width:114px;height:20px;font-size:7px">View all products</div>

    <svg class="shape" style="top:1460px" width="774" height="100" viewBox="0 0 774 100">
      <path d="M0 0 Q300 110 774 32 V100 H0Z" fill="#d6d8df"/>
      <path d="M0 22 Q330 120 774 30 V100 H0Z" fill="#3e5a3e"/>
    </svg>
    <div class="footer" style="top:1560px;height:340px">
      <div class="brand" style="left:0;right:0;justify-content:center;top:30px;font-size:22px"><span>Tolvane</span><span class="brand__dot" style="width:9px;height:9px"></span></div>
      <div class="farm" style="left:57px;width:206px;top:76px;font-size:8px;line-height:1.4">
        <p class="farm__title" style="font-size:9.5px">01 - Lorem Ipsum Farm</p>
        <p>418 Orchard Hollow Rd,<br>Brenly ML 40215</p>
      </div>
      <div class="map" role="img" aria-label="Street map of the farm location" style="left:57px;top:126px;width:206px;height:113px"></div>
      <div class="farm" style="left:284px;width:206px;top:76px;font-size:8px;line-height:1.4">
        <p class="farm__title" style="font-size:9.5px">02 - Lorem Ipsum Farm</p>
        <p>418 Orchard Hollow Rd,<br>Brenly ML 40215</p>
      </div>
      <div class="map" role="img" aria-label="Street map of the farm location" style="left:284px;top:126px;width:206px;height:113px"></div>
      <div class="farm" style="left:511px;width:206px;top:76px;font-size:8px;line-height:1.4">
        <p class="farm__title" style="font-size:9.5px">03 - Lorem Ipsum Farm</p>
        <p>418 Orchard Hollow Rd,<br>Brenly ML 40215</p>
      </div>
      <div class="map" role="img" aria-label="Street map of the farm location" style="left:511px;top:126px;width:206px;height:113px"></div>
      <div class="socials" style="left:353px;top:266px"><span style="width:18px;height:18px"></span><span class="is-active" style="width:18px;height:18px"></span><span style="width:18px;height:18px"></span></div>
      <p class="copyright" style="top:302px;font-size:7.6px">© 2020 <em>Tolvane.</em> All Rights Reserved</p>
    </div>
  </section>

</div>
</body>
</html>
```